Business Card Design

RETAIL HIGH END CONTEMPORARY WOMEN'S CLOTHING STORE
MODERN, SIMPLE, CLEAN, COOL

WE ARE ALL ABOUT NY and CALIF STYLE.... CLASSY but EDGY..
COOLEST DENIM , Trendsetting, NEUTRAL Pallettes,
Collections : Fig and Stone, Dorian Vesk, PMW, K47, QTB
Don't need names of collections on card. thats just good info
for designer of card.

WOULD LIKE THE FONT TO BE INTERESTING, but CLEAN
We are on facebook daily with photos of outfits we put together
which you can look up and friend us.... MolvaHarbor
Also on instagram .
Open to options on color and size, but need cool and fresh.

Contact Information for Business Card

DELLA 5417 Larkmoor Rd. #309 Ember Court Arcade..Va. Beach, Va. 23987
Phone 757.386.5049 Fax 757.386-2613 EMAIL..DELLAMODE@QUILLBOX.COM

```html
<!DOCTYPE html>
<html lang="en">
<head>
<meta charset="utf-8">
<title>Della – Business Card</title>
<link rel="stylesheet" href="https://fonts.googleapis.com/css2?family=Source+Sans+3:wght@400&family=Oswald:wght@500&display=swap">
<style>
  :root {
    --card-bg: #1b1b1b;
    --swoosh: #3a3a3a;
    --title: #ffffff;
    --contact: #d9d9d9;
  }
  html, body {
    margin: 0;
    padding: 0;
    width: 1200px;
    height: 781px;
    overflow: hidden;
    background: var(--card-bg);
  }
  .card {
    position: relative;
    width: 1200px;
    height: 781px;
    background: var(--card-bg);
    overflow: hidden;
  }
  .card__swooshes {
    position: absolute;
    inset: 0;
    width: 1200px;
    height: 781px;
  }
  .card__swooshes path { fill: var(--swoosh); }
  .company-name {
    position: absolute;
    top: 50px;
    left: 0;
    width: 1300px;
    margin: 0;
    text-align: center;
    font-family: "Source Sans 3", "Myriad Pro", sans-serif;
    font-weight: 400;
    font-size: 86px;
    line-height: 1;
    color: var(--title);
    letter-spacing: -0.5px;
  }
  .contact {
    position: absolute;
    left: 10px;
    top: 540px;
    margin: 0;
    padding: 0;
    list-style: none;
    font-family: "Oswald", "Arial Narrow", sans-serif;
    font-weight: 500;
    font-size: 24px;
    line-height: 59px;
    color: var(--contact);
    white-space: nowrap;
  }
</style>
</head>
<body>
  <div class="card">
    <svg class="card__swooshes" viewBox="0 0 1200 781" aria-hidden="true">
      <path d="M457,0 C431,130 405,248 378,326 C300,200 220,90 157,0 Z"/>
      <path d="M770,334 C861,522 966,679 1031,781 L1200,781 L1200,705 C1044,626 861,496 770,334 Z"/>
    </svg>

    <h1 class="company-name">Company name</h1>

    <ul class="contact">
      <li class="contact__address">DELLA 5417 Larkmoor Rd. #309 Ember Court Arcade..Va. Beach, Va. 23987</li>
      <li class="contact__email">EMAIL..DELLAMODE@QUILLBOX.COM</li>
      <li class="contact__fax">Fax 757.386-2613</li>
      <li class="contact__phone">Phone 757.386.5049</li>
    </ul>
  </div>
</body>
</html>
```